Looking for a cool & simple business-card-design for digital agency

Hi!

We are a web agency that offers Reputation Management, Quorvix & Seo Services and software development. We like cool things, we like innovative styles.

We have uploaded our logo.

Project Deadline Extended Reason: Client does not want any designs with the colorful logo. Please send us submissions ONLY with the blac and white logo. What the client would like to see:1) Back of the card: is a silver logo on a black background2) front of the card with all the data, please use white background and black logo thank you Added Friday, May 8, 2015

```html
<!DOCTYPE html>
<html lang="en">
<head>
<meta charset="utf-8">
<title>NetPrime Business Card</title>
<link href="https://fonts.googleapis.com/css2?family=Lato:wght@400;700;900&display=swap" rel="stylesheet">
<style>
  :root {
    --stage: #2a2a2a;
    --card-white: #f7f7f7;
    --ink: #111111;
    --gold: #e2b02a;
    --gold-light: #f0c444;
    --gold-text: #f1bd2e;
    --soft-grey: #6c6c6c;
    --contact-text: #e8e8e8;
  }
  html, body {
    margin: 0;
    width: 1200px;
    height: 873px;
    overflow: hidden;
    background: var(--stage);
    font-family: "Lato", sans-serif;
  }
  .stage {
    position: relative;
    width: 1200px;
    height: 873px;
  }
  .card {
    position: absolute;
    width: 540px;
    height: 309px;
    border-radius: 22px;
    overflow: hidden;
    background: var(--card-white);
    box-shadow: 0 10px 30px rgba(0,0,0,0.5);
  }
  .card-back { left: 40px; top: 160px; }
  .card-front { left: 620px; top: 404px; }
  .card-shapes {
    position: absolute;
    inset: 0;
  }
  .back-brand {
    position: absolute;
    right: 34px;
    bottom: 40px;
    text-align: left;
    border-left: 2px solid var(--ink);
    padding-left: 10px;
  }
  .brand-name {
    font-weight: 900;
    color: var(--ink);
    letter-spacing: 0.5px;
    line-height: 1;
  }
  .brand-tagline {
    font-weight: 400;
    color: var(--ink);
    letter-spacing: 4px;
    text-transform: uppercase;
    line-height: 1.2;
  }
  .back-brand .brand-name { font-size: 30px; }
  .back-brand .brand-tagline { font-size: 10px; }
  .front-brand {
    position: absolute;
    left: 130px;
    top: 44px;
    display: flex;
    align-items: center;
    gap: 12px;
  }
  .brand-square {
    width: 30px;
    height: 30px;
    background: var(--ink);
  }
  .front-brand .brand-text {
    border-left: 2px solid var(--ink);
    padding-left: 10px;
  }
  .front-brand .brand-name { font-size: 42px; }
  .front-brand .brand-tagline { font-size: 13px; letter-spacing: 5px; }
  .holder {
    position: absolute;
    left: 185px;
    width: 270px;
    top: 160px;
    text-align: center;
    color: var(--ink);
  }
  .holder-name { font-size: 19px; font-weight: 900; line-height: 1.1; }
  .holder-role { font-size: 13px; font-weight: 400; }
  .company-line {
    position: absolute;
    left: 26px;
    top: 216px;
    font-size: 15px;
    font-weight: 900;
    color: var(--gold-text);
  }
  .contact-list {
    position: absolute;
    left: 26px;
    top: 238px;
    margin: 0;
    padding: 0;
    list-style: none;
  }
  .contact-list li {
    display: flex;
    align-items: center;
    gap: 10px;
    font-size: 15px;
    color: var(--contact-text);
    height: 21px;
  }
  .contact-icon { width: 12px; height: 12px; flex: none; }
  .corner-brand {
    position: absolute;
    right: 26px;
    top: 222px;
    font-size: 20px;
    font-weight: 900;
    color: var(--contact-text);
  }
</style>
</head>
<body>
<main class="stage">

  <section class="card card-back" aria-label="Card back">
    <div class="back-brand">
      <div class="brand-name">NetPrime</div>
      <div class="brand-tagline">Digitale Strategien</div>
    </div>
  </section>

  <section class="card card-front" aria-label="Card front">
    <svg class="card-shapes" width="540" height="309" viewBox="0 0 540 309" aria-hidden="true">
      <polygon points="0,205 540,205 540,309 0,309" fill="var(--ink)"/>
      <polygon points="455,150 540,150 540,205 420,205" fill="var(--ink)"/>
      <polygon points="150,205 185,152 455,152 420,205" fill="var(--gold)"/>
      <polygon points="120,205 150,205 185,152 170,152" fill="var(--gold-light)"/>
      <polygon points="455,152 470,140 540,140 540,150 455,150" fill="var(--gold-light)"/>
    </svg>

    <div class="front-brand">
      <span class="brand-square"></span>
      <div class="brand-text">
        <div class="brand-name">NetPrime</div>
        <div class="brand-tagline">Digitale Strategien</div>
      </div>
    </div>

    <div class="holder">
      <div class="holder-name">Carla Wendt</div>
      <div class="holder-role">Owner / Founder</div>
    </div>

    <div class="corner-brand">NetPrime</div>

    <div class="company-line">NetPrime Digitale Strategien</div>
    <ul class="contact-list">
      <li>
        <svg class="contact-icon" viewBox="0 0 12 12" aria-hidden="true"><rect x="3" y="0.5" width="6" height="11" rx="1" fill="none" stroke="var(--gold-text)" stroke-width="1.3"/></svg>
        555-014-2297
      </li>
      <li>
        <svg class="contact-icon" viewBox="0 0 12 12" aria-hidden="true"><rect x="0.5" y="2" width="11" height="8" fill="var(--gold-text)"/><polyline points="0.5,2 6,6.5 11.5,2" fill="none" stroke="var(--ink)" stroke-width="1"/></svg>
        carla@netprime.com
      </li>
      <li>
        <svg class="contact-icon" viewBox="0 0 12 12" aria-hidden="true"><path d="M5 7 L7 5 M4 6 L2 8 a1.5 1.5 0 0 0 2 2 L6 8 M8 6 L10 4 a1.5 1.5 0 0 0 -2 -2 L6 4" fill="none" stroke="var(--gold-text)" stroke-width="1.3"/></svg>
        www.netprime.com
      </li>
    </ul>
  </section>

</main>
</body>
</html>
```